Business Card Design

I am an child sleep consultant. I would like the picture to be the background of the card and for my logo to be in the upper right hand corner. Other than that, the design is yours!!

Industry/Entity Type

Business

Contact Information for Business Card

Marla Okonov
Tidewell Nestling
Certified Child Sleep Consultant
(406) 555-0193
tidewellnestling.example

```html
<!DOCTYPE html>
<html lang="en">
<head>
<meta charset="utf-8">
<title>Tidewell Nestling – Business Card</title>
<link rel="stylesheet" href="https://fonts.googleapis.com/css2?family=Open+Sans:wght@400;700&display=swap">
<style>
  :root {
    --backdrop: #9a86b8;
    --card-green: #8cc63f;
    --card-green-light: #c5e48a;
    --card-blue: #12aee4;
    --accent-purple: #8e4fa6;
    --icon-yellow: #f5e61e;
    --ink-white: #ffffff;
    --ink-navy: #1f2a6b;
    --photo-dark: #6d6d6d;
    --photo-light: #c9c9c9;
  }
  * { box-sizing: border-box; margin: 0; padding: 0; }
  html, body { width: 1200px; height: 1000px; overflow: hidden; }
  body {
    background: var(--backdrop);
    font-family: "Open Sans", sans-serif;
    position: relative;
  }
  .card {
    position: absolute;
    left: 250px;
    width: 700px;
    height: 400px;
    overflow: hidden;
    box-shadow: 0 8px 24px rgba(40, 20, 70, 0.25);
  }
  .card--back { top: 70px; background: var(--card-green); }
  .card--front { top: 530px; }
  .card__art { position: absolute; inset: 0; }

  .back-brand {
    position: absolute;
    inset: 0;
    display: flex;
    align-items: center;
    justify-content: center;
    gap: 14px;
  }
  .brand-dot {
    width: 30px; height: 30px; border-radius: 50%;
    background: var(--ink-white);
  }
  .brand-name {
    font-weight: 700;
    color: var(--ink-navy);
    letter-spacing: 0.5px;
  }
  .back-brand .brand-name { font-size: 40px; color: var(--ink-white); }

  .corner-brand {
    position: absolute;
    top: 48px; right: 16px;
    width: 150px;
    text-align: center;
    font-size: 17px;
    line-height: 1.1;
  }

  .contact {
    position: absolute;
    right: 40px;
    top: 212px;
    text-align: right;
    color: var(--ink-white);
  }
  .contact__name { font-size: 27px; font-weight: 700; line-height: 1.1; }
  .contact__company, .contact__title { font-size: 15px; line-height: 1.3; }
  .contact__list { list-style: none; margin-top: 10px; }
  .contact__item {
    display: flex; align-items: center; justify-content: flex-end;
    gap: 10px; font-size: 15px; height: 32px;
  }
  .contact__icon { width: 24px; height: 24px; flex: none; }
</style>
</head>
<body>

  <section class="card card--back" aria-label="Card back">
    <div class="back-brand">
      <span class="brand-dot"></span>
      <span class="brand-name">Tidewell Nestling</span>
    </div>
  </section>

  <section class="card card--front" aria-label="Card front">
    <svg class="card__art" viewBox="0 0 700 400" width="700" height="400">
      <defs>
        <radialGradient id="photoTone" cx="45%" cy="45%" r="70%">
          <stop offset="0" stop-color="var(--photo-light)"/>
          <stop offset="1" stop-color="var(--photo-dark)"/>
        </radialGradient>
        <linearGradient id="curlTone" x1="0" y1="0" x2="1" y2="1">
          <stop offset="0" stop-color="#e8f5c8"/>
          <stop offset="1" stop-color="var(--card-green)"/>
        </linearGradient>
      </defs>
      <rect class="blue-field" width="700" height="400" fill="var(--card-blue)"/>
      <path class="purple-band" d="M0 0 H440 C470 120 450 280 370 400 H0 Z" fill="var(--accent-purple)"/>
      <path class="white-band" d="M0 0 H428 C456 120 436 280 356 400 H0 Z" fill="var(--ink-white)"/>
      <path class="photo-area" role="img" aria-label="Black and white photograph of a smiling baby"
            d="M0 0 H420 C446 120 426 280 346 400 H0 Z" fill="url(#photoTone)"/>
      <path class="green-corner" d="M530 0 H700 V260 C640 230 560 120 530 0 Z" fill="var(--card-green)"/>
      <path class="page-curl" d="M530 0 C560 110 620 200 700 260 C660 190 640 140 620 110 C590 90 560 50 530 0 Z" fill="url(#curlTone)"/>
    </svg>

    <div class="corner-brand brand-name">Tidewell<br>Nestling</div>

    <div class="contact">
      <p class="contact__name">Marla Okonov</p>
      <p class="contact__company">Tidewell Nestling</p>
      <p class="contact__title">Certified Child Sleep Consultant</p>
      <ul class="contact__list">
        <li class="contact__item">
          <svg class="contact__icon" viewBox="0 0 24 24" aria-hidden="true">
            <circle cx="12" cy="12" r="12" fill="var(--icon-yellow)"/>
            <rect x="8.5" y="5" width="7" height="14" rx="1.5" fill="none" stroke="var(--card-blue)" stroke-width="1.6"/>
            <circle cx="12" cy="16.5" r="0.9" fill="var(--card-blue)"/>
          </svg>
          <span>(406) 555-0193</span>
        </li>
        <li class="contact__item">
          <svg class="contact__icon" viewBox="0 0 24 24" aria-hidden="true">
            <circle cx="12" cy="12" r="12" fill="var(--icon-yellow)"/>
            <path d="M6 12 L12 6.5 L18 12 M8 11 V17.5 H16 V11" fill="none" stroke="var(--card-blue)" stroke-width="1.6" stroke-linejoin="round"/>
          </svg>
          <span>tidewellnestling.example</span>
        </li>
        <li class="contact__item">
          <svg class="contact__icon" viewBox="0 0 24 24" aria-hidden="true">
            <circle cx="12" cy="12" r="12" fill="var(--icon-yellow)"/>
            <rect x="6" y="8" width="12" height="8.5" fill="none" stroke="var(--card-blue)" stroke-width="1.5"/>
            <path d="M6 8 L12 13 L18 8" fill="none" stroke="var(--card-blue)" stroke-width="1.5"/>
          </svg>
          <span>marla@tidewellnestling.example</span>
        </li>
      </ul>
    </div>
  </section>

</body>
</html>
```